Business Cards for Logistics Company

Looking to update Business Card Design.
Logo is attached. Blue background is not a part of the logo, you can remove it in layers.

Company: Harbor Crest Freightways
Industry: Logistics, Container Shipping

Address:
418 Willow Bend Ave
Bayonne NJ 07419

Phones:
p. 201-555-0143
f. 201-555-0178
c. very by person's name

Website: www.hcfroute.example

Design has to include person's name and position.
OLD Design is included.

B2B

Business

Card Size (non standard): 1039 x 697 pixels, 300dpi
Template is attached.

Font styles to use
Serif
Sans Serif

```html
<!DOCTYPE html>
<html lang="en">
<head>
<meta charset="utf-8">
<title>Harbor Crest Freightways – Business Cards</title>
<link rel="stylesheet" href="https://fonts.googleapis.com/css2?family=Open+Sans:wght@400;700&family=PT+Serif:wght@700&display=swap">
<style>
  :root {
    --page-bg: #e9e6e1;
    --navy-top: #4a65a6;
    --navy-mid: #1f3a82;
    --navy-deep: #15286a;
    --card-white: #ffffff;
    --ink-white: #ffffff;
    --ink-soft: #dbe3f5;
    --brand-blue: #2f63b8;
    --brand-grey: #6a7b93;
    --tagline-navy: #1c2f63;
    --rule: rgba(255,255,255,0.45);
  }
  * { box-sizing: border-box; margin: 0; padding: 0; }
  html, body { width: 1200px; height: 913px; overflow: hidden; }
  body {
    background: var(--page-bg);
    font-family: "Open Sans", Arial, sans-serif;
    position: relative;
  }
  .card {
    position: absolute;
    top: 282px;
    width: 520px;
    height: 349px;
    border-radius: 6px;
    box-shadow: 0 10px 28px rgba(0,0,0,0.22);
    overflow: hidden;
  }
  .card--front {
    left: 60px;
    background: linear-gradient(160deg, var(--navy-top) 0%, var(--navy-mid) 45%, var(--navy-deep) 100%);
    color: var(--ink-white);
  }
  .card--back {
    left: 620px;
    background: var(--card-white);
  }

  /* brand lockup */
  .brand { position: absolute; display: flex; align-items: center; gap: 14px; }
  .brand__mark { flex: none; }
  .brand__name {
    font-weight: 400;
    letter-spacing: 0.22em;
    text-transform: uppercase;
    line-height: 1.25;
  }
  .card--front .brand { left: 34px; top: 198px; }
  .card--front .brand__mark { width: 62px; height: 62px; background: var(--brand-blue); }
  .card--front .brand__name { font-size: 13px; color: var(--ink-white); width: 170px; }
  .card--back .brand { left: 60px; top: 120px; }
  .card--back .brand__mark { width: 92px; height: 92px; background: var(--brand-blue); }
  .card--back .brand__name { font-size: 21px; color: var(--brand-grey); width: 300px; }

  /* divider */
  .divider {
    position: absolute;
    left: 262px; top: 44px;
    width: 1px; height: 240px;
    background: var(--rule);
  }

  /* contact block */
  .contact { position: absolute; left: 284px; top: 46px; }
  .contact__name { font-size: 19px; font-weight: 700; line-height: 1.2; }
  .contact__role, .contact__address {
    font-size: 11.5px; color: var(--ink-soft); line-height: 1.45;
  }
  .contact__role { margin-bottom: 1px; }
  .contact__list { list-style: none; margin-top: 16px; }
  .contact__item {
    display: flex; align-items: center; gap: 8px;
    font-size: 11.5px; line-height: 1.55; color: var(--ink-white);
  }
  .contact__icon { width: 11px; height: 11px; flex: none; }

  .tagline {
    position: absolute;
    left: 60px; bottom: 62px;
    font-family: "PT Serif", Georgia, serif;
    font-weight: 700;
    font-size: 13px;
    color: var(--tagline-navy);
  }
</style>
</head>
<body>

<section class="card card--front" aria-label="Business card front">
  <div class="brand">
    <span class="brand__mark"></span>
    <span class="brand__name">Harbor Crest Freightways</span>
  </div>

  <span class="divider"></span>

  <div class="contact">
    <p class="contact__name">Dmitri Varlamov</p>
    <p class="contact__role">General Manager</p>
    <p class="contact__address">418 Willow Bend Ave<br>Bayonne NJ 07419</p>
    <ul class="contact__list">
      <li class="contact__item">
        <svg class="contact__icon" viewBox="0 0 12 12" fill="currentColor"><path d="M2.5 1 4.5 1 5.3 3.6 4 4.6C4.7 6 6 7.3 7.4 8L8.4 6.7 11 7.5 11 9.5C11 10.3 10.3 11 9.5 11 5 11 1 7 1 2.5 1 1.7 1.7 1 2.5 1Z"/></svg>
        201-555-0143
      </li>
      <li class="contact__item">
        <svg class="contact__icon" viewBox="0 0 12 12" fill="currentColor"><rect x="3" y="1" width="6" height="3"/><rect x="1" y="4.5" width="10" height="4.5" rx="1"/><rect x="3" y="8" width="6" height="3"/></svg>
        201-555-0178
      </li>
      <li class="contact__item">
        <svg class="contact__icon" viewBox="0 0 12 12" fill="none" stroke="currentColor" stroke-width="1.2"><rect x="3" y="0.8" width="6" height="10.4" rx="1"/><line x1="5" y1="9.4" x2="7" y2="9.4"/></svg>
        646-555-0192
      </li>
      <li class="contact__item">
        <svg class="contact__icon" viewBox="0 0 12 12" fill="none" stroke="currentColor" stroke-width="1.2"><rect x="1" y="2.5" width="10" height="7"/><path d="M1 2.5 6 6.5 11 2.5"/></svg>
        dispatch@hcfroute.example
      </li>
      <li class="contact__item">
        <svg class="contact__icon" viewBox="0 0 12 12" fill="none" stroke="currentColor" stroke-width="1"><circle cx="6" cy="6" r="5"/><ellipse cx="6" cy="6" rx="2.2" ry="5"/><line x1="1" y1="6" x2="11" y2="6"/></svg>
        www.hcfroute.example
      </li>
    </ul>
  </div>
</section>

<section class="card card--back" aria-label="Business card back">
  <div class="brand">
    <span class="brand__mark"></span>
    <span class="brand__name">Harbor Crest Freightways</span>
  </div>
  <p class="tagline">Ocean &amp; Air Freight · Loading &amp; Storage · Multimodal Transport</p>
</section>

</body>
</html>
```